Cover Photo Design Needed for Business

We need a Facebook cover photo design for a new company called "Quillmarestan". Our goal is to enable your success through the free exchange of wisdom and tools through other entrepreneur's. For those looking to take further steps, we offer several paid services that can help you start, manage, and grow your venture. Were looking for something new and creative.

Industry/Entity Type

Business

Requirements
Nice to have
• If it goes with the cover photo we would like an arrow pointing to the like button.

```html
<!DOCTYPE html>
<html lang="en">
<head>
<meta charset="utf-8">
<title>Quillmarestan cover</title>
<link rel="stylesheet" href="https://fonts.googleapis.com/css2?family=Questrial&display=swap">
<style>
  :root {
    --page-bg: #eceef2;
    --lime: #a6c92e;
    --lime-light: #c4dc45;
    --white: #ffffff;
    --charcoal: #5d5e61;
    --tile-circle: #86878a;
    --border: #d3d6db;
  }
  * { box-sizing: border-box; margin: 0; padding: 0; }
  html, body {
    width: 1200px;
    height: 723px;
    overflow: hidden;
    background: var(--page-bg);
    font-family: "Questrial", "Century Gothic", sans-serif;
  }
  .canvas {
    position: relative;
    width: 1200px;
    height: 723px;
  }
  .cover {
    position: absolute;
    left: 50px;
    top: 60px;
    width: 1100px;
    height: 407px;
    overflow: hidden;
  }
  .cover-backdrop {
    position: absolute;
    inset: 0;
    width: 100%;
    height: 100%;
  }
  .cover-title {
    position: absolute;
    left: 30px;
    top: 46px;
    font-size: 88px;
    font-weight: 400;
    line-height: 1;
    color: var(--white);
    letter-spacing: -0.5px;
    white-space: nowrap;
  }
  .topic-list {
    position: absolute;
    top: 146px;
    list-style: none;
    font-size: 26px;
    line-height: 26px;
    color: var(--white);
    white-space: nowrap;
  }
  .topic-list li::before,
  .topic-list .inline-topic::before {
    content: "•";
    color: var(--lime-light);
    margin-right: 7px;
    font-size: 18px;
    vertical-align: 3px;
  }
  .topic-list.left { left: 34px; }
  .topic-list.right { left: 310px; }
  .topic-list .inline-topic { margin-left: 12px; }
  .cover-url {
    position: absolute;
    left: 272px;
    top: 336px;
    font-size: 27px;
    color: var(--white);
    white-space: nowrap;
  }
  .cover-url .domain { color: var(--lime-light); }
  .profile-tile {
    position: absolute;
    left: 80px;
    top: 330px;
    width: 222px;
    height: 222px;
    background: var(--lime);
    border: 5px solid var(--white);
    box-shadow: 0 0 0 1px var(--border);
  }
  .profile-mark {
    position: absolute;
    left: 50%;
    top: 24px;
    width: 118px;
    height: 118px;
    margin-left: -59px;
    border-radius: 50%;
    background: var(--tile-circle);
  }
  .profile-name {
    position: absolute;
    left: 0;
    right: 0;
    bottom: 22px;
    text-align: center;
    font-size: 23px;
    color: var(--charcoal);
  }
</style>
</head>
<body>
<main class="canvas">
  <section class="cover">
    <svg class="cover-backdrop" viewBox="0 0 1100 407" preserveAspectRatio="none" aria-hidden="true">
      <defs>
        <linearGradient id="lime-sweep" x1="0" y1="0" x2="1" y2="0">
          <stop offset="0" stop-color="#a9cb30"/>
          <stop offset="1" stop-color="#c7de4c"/>
        </linearGradient>
        <linearGradient id="grey-field" x1="0" y1="0" x2="0" y2="1">
          <stop offset="0" stop-color="#8d8e91"/>
          <stop offset="1" stop-color="#7f8083"/>
        </linearGradient>
      </defs>
      <rect width="1100" height="407" fill="url(#grey-field)"/>
      <polygon points="780,0 1100,0 1100,407 1000,407" fill="url(#lime-sweep)"/>
      <polygon points="764,0 780,0 1000,407 984,407" fill="#ffffff"/>
    </svg>

    <h1 class="cover-title">Quillmarestan</h1>

    <ul class="topic-list left">
      <li>Education &amp; careers</li>
      <li>Finance</li>
      <li>Manage &amp; Grow</li>
      <li>Online Business</li>
    </ul>
    <ul class="topic-list right">
      <li>Sales &amp; Marketing</li>
      <li>Small Business</li>
      <li>Social Media</li>
      <li>Start-Up<span class="inline-topic">Technology</span></li>
    </ul>

    <p class="cover-url">www.<span class="domain">quillmarestan</span>.com</p>
  </section>

  <aside class="profile-tile">
    <span class="profile-mark" aria-hidden="true"></span>
    <p class="profile-name">Quillmarestan</p>
  </aside>
</main>
</body>
</html>
```